Equine Podcast Cover Art Design

We need catchy cover art for a horse related podcast "Ride Onward Together"
Brief show description"
Whether you want to ride to experience horses, develop yourself to the next level as a horseman/horsewoman or ride to improve your physical and mental health, we are committed to helping you Ride Onward TogetherĀ®. Join us as we explore the nuance of equine management and sports as well as interview industry professionals to provide you with the knowledge necessary to be a better partner for your equine friends.
I have uploaded two existing logos we use for various purposes to give you an idea of existing style.
Target Market(s)
Horse owners and other equine professionals
Look and feel
Each slider illustrates characteristics of the customer's brand and the style your logo design should communicate.

```html
<!DOCTYPE html>
<html lang="en">
<head>
<meta charset="utf-8">
<title>Ride Onward Together Podcast Cover</title>
<link href="https://fonts.googleapis.com/css2?family=Anton&family=Oswald:wght@200;400&display=swap" rel="stylesheet">
<style>
  :root {
    --cover-red: #b02335;
    --ink-white: #ffffff;
    --mic-navy: #2f3566;
    --page-bg: #ffffff;
    --horse-dark: #5a2a14;
    --horse-mid: #9a4a22;
    --rider-red: #c8322f;
  }
  * { margin: 0; padding: 0; box-sizing: border-box; }
  html, body {
    width: 1200px;
    height: 807px;
    overflow: hidden;
    background: var(--page-bg);
  }
  .cover {
    position: absolute;
    left: 240px;
    top: 43px;
    width: 720px;
    height: 720px;
    background: var(--cover-red);
    overflow: hidden;
  }
  .title {
    position: absolute;
    left: 40px;
    top: 34px;
    color: var(--ink-white);
    font-family: "Anton", sans-serif;
    text-transform: uppercase;
    line-height: 0.92;
  }
  .title-line { display: block; letter-spacing: -1px; }
  .title-line--short { font-size: 150px; }
  .title-line--mid { font-size: 128px; }
  .title-line--big { font-size: 150px; letter-spacing: -2px; }
  .letter-o { position: relative; display: inline-block; }
  .mic-icon {
    position: absolute;
    left: 50%;
    top: 52%;
    width: 46px;
    height: 84px;
    transform: translate(-50%, -50%);
  }
  .podcast-label {
    position: absolute;
    left: 44px;
    top: 640px;
    color: var(--ink-white);
    font-family: "Oswald", sans-serif;
    font-weight: 200;
    font-size: 38px;
    letter-spacing: 34px;
  }
  .farm-mark {
    position: absolute;
    right: 40px;
    top: 40px;
    display: flex;
    align-items: center;
    gap: 10px;
    color: var(--ink-white);
    font-family: "Anton", sans-serif;
    font-size: 20px;
    letter-spacing: 1px;
    text-transform: uppercase;
  }
  .farm-mark-dot {
    width: 22px;
    height: 22px;
    border-radius: 50%;
    background: var(--ink-white);
  }
  .rider-photo {
    position: absolute;
    left: 440px;
    top: 410px;
    width: 280px;
    height: 310px;
    border-radius: 120px 40px 0 60px;
    background: linear-gradient(160deg, var(--rider-red) 0%, var(--horse-mid) 40%, var(--horse-dark) 100%);
  }
</style>
</head>
<body>
  <main class="cover">
    <h1 class="title">
      <span class="title-line title-line--short">Ride</span>
      <span class="title-line title-line--mid">Onward</span>
      <span class="title-line title-line--big">T<span class="letter-o">O<svg class="mic-icon" viewBox="0 0 46 84" aria-hidden="true">
        <rect x="11" y="0" width="24" height="46" rx="12" fill="var(--mic-navy)"/>
        <path d="M4 34 a19 19 0 0 0 38 0" fill="none" stroke="var(--mic-navy)" stroke-width="5"/>
        <rect x="20.5" y="53" width="5" height="20" fill="var(--mic-navy)"/>
        <rect x="9" y="73" width="28" height="6" rx="2" fill="var(--mic-navy)"/>
      </svg></span>GETHER</span>
    </h1>
    <p class="podcast-label">PODCAST</p>
    <div class="farm-mark">
      <span class="farm-mark-dot"></span>
      <span class="farm-mark-name">Still Meadow Farm</span>
    </div>
    <div class="rider-photo" role="img" aria-label="Photo of a rider in a red jacket and helmet jumping a chestnut horse"></div>
  </main>
</body>
</html>
```